I require a set of preaching screens for our Easter weekend.

1. Good Friday Service Title: Still Lanterns
2. Easter Sunday Service Title Bright Harbor
3. Message Title Screen Title Bright Harbor
Overview
We need a set of clean, minimal screen graphics for 3 service sermon series called Bright Harbor
All screens must be delivered at 1920x1080px (16:9), suitable for projection in a church auditorium.

Design style
Minimal and clean. Uncluttered. Strong typography. Subtle use of imagery or texture — nothing busy or overly decorative.

The tone should feel thoughtful and weighty without being dark or heavy.

Subtitle: Letters Written Beside a Quiet Harbor Gate
Date range: 1 March – 5 April

Branding
No existing branding to match. Designer has creative freedom on colour palette and typography, provided the overall feel remains minimal and clean.
What to avoid
Busy backgrounds or heavy textures
All files in PNG at 1920x1080px
Editable source files (PSD or AI)

Please use images below as you feel is appropriate - we have permission for these - We want to see a at least three options for these screens to .

We need designs within 3 days

```html
<!DOCTYPE html>
<html lang="en">
<head>
<meta charset="utf-8">
<title>Bright Harbor – Screen Options</title>
<link rel="stylesheet" href="https://fonts.googleapis.com/css2?family=Cinzel:wght@500;600;700&display=swap">
<style>
  :root {
    --board: #e9e8e4;
    --brown: #7a4320;
    --bronze: #8a5a22;
    --ink: #231a12;
    --cream: #f3efe4;
    --sky-top: #b8dcf6;
    --sky-mid: #d9effa;
    --sky-low: #fbf6e8;
    --tan-light: #dcc8a8;
    --tan-dark: #c6a87f;
    --glow: #ffd766;
  }
  * { margin: 0; padding: 0; box-sizing: border-box; }
  html, body { width: 1200px; height: 1200px; overflow: hidden; }
  body { background: var(--board); font-family: "Cinzel", serif; position: relative; }

  .screen {
    position: absolute; left: 335px; width: 529px; height: 297px;
    overflow: hidden;
    box-shadow: 0 6px 14px rgba(0,0,0,.28);
  }
  .screen--still { top: 101px; background: linear-gradient(90deg, #fff 0%, #fff 55%, var(--cream) 100%); }
  .screen--sky { top: 451px; background: linear-gradient(180deg, var(--sky-top) 0%, var(--sky-mid) 40%, var(--sky-low) 100%); }
  .screen--gold { top: 807px; background: linear-gradient(90deg, var(--tan-light) 0%, var(--tan-dark) 100%); }

  .art { position: absolute; }
  .line, .title, .subtitle, .dates { position: absolute; text-align: center; }
  .divider { position: absolute; height: 1px; }

  /* Still Lanterns */
  .screen--still .art {
    left: 9px; top: 73px; width: 202px; height: 164px;
    background: radial-gradient(ellipse at 50% 55%, #e9dcc2 0%, #f1e8d6 45%, rgba(255,255,255,0) 72%);
  }
  .screen--still .title { left: 192px; width: 316px; color: var(--brown); font-weight: 700; line-height: 1; }
  .screen--still .title--top { top: 30px; font-size: 44px; }
  .screen--still .title--main { top: 80px; font-size: 52px; }
  .screen--still .subtitle { left: 192px; width: 316px; top: 152px; color: var(--brown); font-size: 19px; font-weight: 600; line-height: 26px; }
  .screen--still .divider { left: 230px; width: 180px; top: 226px; background: linear-gradient(90deg, transparent, var(--brown), transparent); }
  .screen--still .dates { left: 192px; width: 316px; top: 244px; color: var(--brown); font-size: 24px; font-weight: 600; }

  /* Bright Harbor – sky */
  .screen--sky .title { left: 0; width: 100%; top: 16px; color: var(--bronze); font-size: 52px; font-weight: 700; }
  .screen--sky .subtitle { left: 0; width: 100%; top: 102px; color: var(--bronze); font-size: 16.5px; font-weight: 600; }
  .screen--sky .divider { left: 170px; width: 190px; top: 136px; background: linear-gradient(90deg, transparent, var(--bronze), transparent); }
  .screen--sky .dates { left: 0; width: 100%; top: 144px; color: var(--bronze); font-size: 24px; font-weight: 600; }
  .screen--sky .art {
    left: 143px; top: 176px; width: 242px; height: 121px;
    background: radial-gradient(ellipse at 50% 100%, rgba(255,255,255,0) 35%, rgba(168,104,52,.55) 52%, rgba(168,104,52,0) 70%);
  }

  /* Bright Harbor – gold */
  .screen--gold .title { color: var(--ink); font-weight: 700; line-height: 1; text-align: left; }
  .screen--gold .title--top { left: 30px; top: 30px; font-size: 46px; }
  .screen--gold .title--main { left: 112px; top: 82px; font-size: 58px; }
  .screen--gold .subtitle { left: 10px; width: 360px; top: 168px; color: var(--ink); font-size: 18px; font-weight: 600; line-height: 25px; }
  .screen--gold .divider { left: 100px; width: 180px; top: 229px; background: linear-gradient(90deg, transparent, var(--ink), transparent); }
  .screen--gold .dates { left: 10px; width: 360px; top: 248px; color: var(--ink); font-size: 24px; font-weight: 600; }
  .screen--gold .art {
    left: 400px; top: 0; width: 110px; height: 297px;
    background: radial-gradient(ellipse at 55% 30%, rgba(255,240,170,.95) 0%, rgba(255,215,102,.6) 25%, rgba(255,215,102,0) 60%);
  }
</style>
</head>
<body>
  <section class="screen screen--still">
    <div class="art" role="img" aria-label="Wooden cross draped with a cream cloth"></div>
    <div class="title title--top">Still</div>
    <div class="title title--main">Lanterns</div>
    <p class="subtitle">Letters Written Beside a<br>Quiet Harbor Gate</p>
    <div class="divider"></div>
    <p class="dates">1 March – 5 April</p>
  </section>

  <section class="screen screen--sky">
    <h1 class="title">Bright Harbor</h1>
    <p class="subtitle">Letters Written Beside a Quiet Harbor Gate</p>
    <div class="divider"></div>
    <p class="dates">1 March – 5 April</p>
    <div class="art" role="img" aria-label="Crown of thorns rising from the bottom edge"></div>
  </section>

  <section class="screen screen--gold">
    <div class="title title--top">Bright</div>
    <div class="title title--main">Harbor</div>
    <p class="subtitle">Letters Written Beside a<br>Quiet Harbor Gate</p>
    <div class="divider"></div>
    <p class="dates">1 March – 5 April</p>
    <div class="art" role="img" aria-label="Hanging crucifix silhouette in a beam of golden light"></div>
  </section>
</body>
</html>
```